Modern Business Card For A Digital Advertising Company

I'll be print on the Tarn Prints Velour paper http://us.tarnprints.example/products/velour/business-cards.html
Need's to be modern and use the color palette of the logo or gray scales. I think integrating the pixelation of the logo in to the card and having it wrap from one side to the other could be interesting. My company provides ad operations, web development, and number of other services to websites around the world. You can see my website at http://www.pixelharbor.example
Contact info on the card needs to have
Dana Welloby
President
p.555.318.4406
dana@pixelharbor.example
http://www.pixelharbor.example
Doesn't necessarily need to be in that order
Target Market(s)
Website owners
Industry/Entity Type
Business
Look and feel

```html
<!DOCTYPE html>
<html lang="en">
<head>
<meta charset="utf-8">
<title>Pixel Harbor — Business Card</title>
<link href="https://fonts.googleapis.com/css2?family=Tinos:wght@400&display=swap" rel="stylesheet">
<style>
  :root {
    --band-top: #a3a2a3;
    --band-bottom: #c6c5c6;
    --card-lower: #e1e0e0;
    --divider-dark: #3e3e3e;
    --brand-green: #8dc63f;
    --name-green: #5f8a3d;
    --title-light: #ececec;
    --contact-ink: #444444;
  }
  html, body {
    margin: 0;
    padding: 0;
    width: 1200px;
    height: 700px;
    overflow: hidden;
    background: var(--card-lower);
  }
  .card {
    position: relative;
    width: 1200px;
    height: 700px;
    overflow: hidden;
    font-family: "Tinos", "Times New Roman", serif;
    background: var(--card-lower);
  }
  .card__upper-band {
    position: absolute;
    left: 0; top: 0;
    width: 1200px;
    height: 372px;
    background: linear-gradient(to bottom, var(--band-top) 0%, var(--band-bottom) 88%, #b9b8b9 94%, var(--divider-dark) 100%);
  }
  .card__divider-glow {
    position: absolute;
    left: 0; top: 372px;
    width: 1200px;
    height: 14px;
    background: linear-gradient(to bottom, rgba(60,60,60,0.35), rgba(60,60,60,0));
  }
  .brand {
    position: absolute;
    left: 48px;
    top: 560px;
    display: flex;
    align-items: center;
    gap: 22px;
  }
  .brand__square {
    width: 58px;
    height: 58px;
    background: var(--brand-green);
  }
  .brand__name {
    font-size: 72px;
    line-height: 1;
    color: var(--brand-green);
    font-weight: 400;
    white-space: nowrap;
  }
  .person {
    position: absolute;
    left: 633px;
    top: 112px;
  }
  .person__name {
    margin: 0;
    font-size: 56px;
    font-weight: 400;
    line-height: 1;
    color: var(--name-green);
  }
  .person__title {
    margin: 8px 0 0 2px;
    font-size: 23px;
    line-height: 1;
    color: var(--title-light);
  }
  .contact {
    position: absolute;
    left: 633px;
    top: 380px;
    margin: 0;
    padding: 0;
    list-style: none;
    font-size: 31px;
    line-height: 45px;
    color: var(--contact-ink);
  }
</style>
</head>
<body>
  <main class="card">
    <div class="card__upper-band"></div>
    <div class="card__divider-glow"></div>

    <div class="brand">
      <span class="brand__square"></span>
      <span class="brand__name">Pixel Harbor</span>
    </div>

    <header class="person">
      <h1 class="person__name">Dana Welloby</h1>
      <p class="person__title">President</p>
    </header>

    <ul class="contact">
      <li class="contact__phone">p.555.318.4406</li>
      <li class="contact__email">dana@pixelharbor.example</li>
      <li class="contact__web">http://www.pixelharbor.example</li>
    </ul>
  </main>
</body>
</html>
```